Brix2Key Header

I want a professional Letterhead for my law firm. I'm attaching the letterhead I currently use in Word and PDF form. I'm also attaching my logo, and an example header that I like.

```html
<!DOCTYPE html>
<html lang="en">
<head>
<meta charset="utf-8">
<title>Brix2Key Letterhead</title>
<link href="https://fonts.googleapis.com/css2?family=Montserrat:wght@400;500;600;900&display=swap" rel="stylesheet">
<style>
  :root {
    --backdrop: #d6d6d8;
    --paper: #ececee;
    --ink-dark: #26262b;
    --ink-body: #7b7b80;
    --ink-meta: #55555a;
    --brand-blue: #0d5aa7;
    --brand-green: #4b8a4e;
    --band-text: #f2f2f2;
  }
  * { box-sizing: border-box; margin: 0; padding: 0; }
  html, body {
    width: 1184px; height: 1200px; overflow: hidden;
    background: var(--backdrop);
    font-family: "Montserrat", Arial, sans-serif;
  }
  .letterhead {
    position: absolute; left: 182px; top: 20px;
    width: 820px; height: 1160px;
    background: var(--paper);
    overflow: hidden;
  }
  .stripe { position: absolute; right: 0; height: 5px; }
  .stripe--blue { top: 54px; left: 193px; background: var(--brand-blue); }
  .stripe--green { top: 63px; left: 193px; background: var(--brand-green); }
  .contact-band {
    position: absolute; top: 74px; left: 308px; right: 0; height: 48px;
    background: var(--ink-dark);
  }
  .brand-name {
    position: absolute; left: 54px; top: 76px;
    font-family: "Montserrat", Arial, sans-serif;
    font-weight: 900; font-size: 40px; line-height: 44px;
    letter-spacing: -0.5px; color: var(--ink-dark);
  }
  .contact-list {
    position: absolute; left: 443px; top: 80px;
    display: grid; grid-template-columns: auto auto; column-gap: 14px; row-gap: 3px;
    font-family: Arial, Helvetica, sans-serif; font-size: 13px; line-height: 15px;
    color: var(--band-text); list-style: none;
  }
  .contact-list li { display: flex; align-items: center; gap: 6px; }
  .contact-list svg { width: 11px; height: 11px; fill: var(--band-text); }
  .recipient { position: absolute; left: 82px; top: 256px; }
  .recipient__label { font-size: 13.5px; font-weight: 500; letter-spacing: 2px; color: var(--ink-dark); }
  .recipient__name { margin-top: 6px; font-size: 13px; font-weight: 500; color: var(--brand-blue); }
  .recipient__address { margin-top: 5px; font-size: 10px; line-height: 18.5px; color: var(--ink-body); font-style: normal; }
  .letter-date { position: absolute; right: 88px; top: 262px; font-size: 10px; color: var(--ink-meta); }
  .letter-body {
    position: absolute; left: 82px; top: 414px; width: 654px;
    font-size: 11px; line-height: 14.6px; color: var(--ink-body);
    text-align: justify;
  }
  .letter-body p + p { margin-top: 14.6px; }
  .signature-mark {
    position: absolute; left: 82px; top: 824px; width: 140px; height: 28px;
    background: linear-gradient(90deg, #dcdce0, #e6e6e9);
    border-radius: 3px;
  }
  .signatory { position: absolute; left: 81px; top: 863px; }
  .signatory__name { font-size: 12px; font-weight: 500; color: var(--ink-dark); }
  .signatory__title { margin-top: 3px; font-size: 9.5px; color: var(--ink-body); }
  .firm-footer {
    position: absolute; left: 0; right: 0; top: 1106px;
    text-align: center; font-family: Arial, Helvetica, sans-serif; font-size: 13.5px; line-height: 17px;
  }
  .firm-footer__name { font-weight: 700; color: var(--brand-blue); }
  .firm-footer__address { color: var(--ink-dark); }
</style>
</head>
<body>
  <main class="letterhead">
    <div class="stripe stripe--blue"></div>
    <div class="stripe stripe--green"></div>
    <div class="contact-band"></div>
    <div class="brand-name">BRIX2KEY</div>
    <ul class="contact-list">
      <li><svg viewBox="0 0 24 24"><path d="M6.6 10.8a15 15 0 0 0 6.6 6.6l2.2-2.2a1 1 0 0 1 1-.25 11.4 11.4 0 0 0 3.6.57 1 1 0 0 1 1 1V20a1 1 0 0 1-1 1A17 17 0 0 1 3 4a1 1 0 0 1 1-1h3.5a1 1 0 0 1 1 1c0 1.25.2 2.45.57 3.57a1 1 0 0 1-.25 1z"/></svg>(800) 555-0142</li>
      <li><svg viewBox="0 0 24 24"><path d="M6 2h12v6H6zM3 9h18v9h-3v4H6v-4H3zm5 7v4h8v-4z"/></svg>(512) 555-0187</li>
      <li><svg viewBox="0 0 24 24"><path d="M2 5h20v14H2zm2 2v.5l8 5 8-5V7z"/></svg>HELLO@BRIX2KEY.NET</li>
      <li><svg viewBox="0 0 24 24"><path d="M12 2a10 10 0 1 0 0 20 10 10 0 0 0 0-20zm0 2c1.2 1.4 2 3.5 2.2 6H9.8C10 7.5 10.8 5.4 12 4zM4.1 13h3.7c.1 2.3.7 4.4 1.7 6A8 8 0 0 1 4.1 13zm0-2A8 8 0 0 1 9.5 5c-1 1.6-1.6 3.7-1.7 6zm5.7 2h4.4c-.2 2.5-1 4.6-2.2 6-1.2-1.4-2-3.5-2.2-6zm4.7 6c1-1.6 1.6-3.7 1.7-6h3.7a8 8 0 0 1-5.4 6zm1.7-8c-.1-2.3-.7-4.4-1.7-6a8 8 0 0 1 5.4 6z"/></svg>WWW.BRIX2KEY.COM</li>
    </ul>

    <section class="recipient">
      <h2 class="recipient__label">TO</h2>
      <p class="recipient__name">Dana Pellerin</p>
      <address class="recipient__address">Human Resources<br>Northvale Systems Inc.<br>2280-B Harlow Road, Westbrook<br>W42 USA</address>
    </section>
    <p class="letter-date">Friday, 01/01/2018</p>

    <article class="letter-body">
      <p>Lorem ipsum dolor sit amet, consectetuer adipiscing elit, sed diam nonmmy nibh euismod tincidunt ut laoreet dolore magna aliquam erat volutpat. Ut wisi enim ad minim veniam, quis nostrud exerci tationmcorper suscipit lobortis nisl ut aliquip ex ea commodo consequat. Duis autem vel eum iriure dolor in hendrerit in vulputate velit esse molestie consequat, vel illum dolore eu feugiat nulla facilisis at vero eros et accumsan et iusto odio dignissim qui blandit praesent luptatum zzril delenit augue duis dolore te feugait nulla facilisi.</p>
      <p>Nam liber tempor cum soluta nobis eleifend option congue nihil imprdiet doming id quod mazim placerat facer possim assum. Typi non habent claritatem insitam;</p>
      <p>Est usus legentis in iis qui facit eorum claritatem.</p>
      <p>Investigationes demonstraverunt lectores legere me lius quod ii legunt saepius. Claritas est etiam processus dynamicus, qui sequitur mutationem consuetudium lectorum. Mirum est notare quam littera gothica, quam nunc putamus parum claram, anteposuerit litterarum formas humanitatis per seacula quarta decima et quinta decima. Eodem modo typi, qui nunc nobis videntur parum clari, fiant sollemnes in futurum.</p>
      <p>consectetuer adipiscing elit, sed diam nonummy nibh euismod tincidunt ut laoreet dolore magna aliquam erat volutpat. Ut wisi enim ad minim veniam, quis nostrud exerci tation ullamcorper suscipit lobortis nisl ut aliquip ex ea commodo consequat. Duis autem vel eum iriure dolor in hendrerit in vulputate velit esse molestie consequat, vel illum dolore eu feugiat nulla facilisis at vero eros et accumsan et iusto odio dignissim qui blandit praesent luptatum zzril delenit augue duis dolore te feugait nulla facilisi.</p>
      <p>Nam liber tempor cum soluta nobis eleifend option congue nihil imperdiet .</p>
    </article>

    <div class="signature-mark" role="img" aria-label="Handwritten signature of Adrian Cole"></div>
    <section class="signatory">
      <p class="signatory__name">Adrian Cole</p>
      <p class="signatory__title">Managing Director</p>
    </section>

    <footer class="firm-footer">
      <p class="firm-footer__name">RAFAEL T. OKONKWO III, ATTORNEY AT LAW, PLLC</p>
      <p class="firm-footer__address">4420 LINDEN AVENUE SUITE 200 AUSTIN, TEXAS 78701</p>
    </footer>
  </main>
</body>
</html>
```